Web Design Project (uncoded)

About Us
ZipRoam is a telecom startup and is looking to launch its website.
ZipRoam specializes in providing communication solutions to the travel market. Our mission is to develop cost effective communication products and solutions for the international traveler.
Our simple vision of "every hotel should have a mobile phone in the guest rooms", led us to develop a pathbreaking & cost effective mobile phone. With full integration capabilities with the hotels property management system, location based marketing, user locator and other features, this product is unique in addressing the hospitality segment.
The website is targeted at hotel owners and property management companies.
The website should have a young contemporary and a funky look, in line with the name.
Please find attached our logo (for the colors etc.). (attached now).
We would like to receive the design for a home page and an inside page for the website.
Site map would be as follows: Home, About Us, Solutions, Contact us
Thanks and look forward,
Tomas
Target Market(s)
Hotel decision makers
Industry/Entity Type
Property Management
Look and feel
Each slider illustrates characteristics of the customer's brand and the style your logo design should communicate.

```html
<!DOCTYPE html>
<html lang="en">
<head>
<meta charset="utf-8">
<title>ZipRoam – Home</title>
<link href="https://fonts.googleapis.com/css2?family=Squada+One&family=Gelasio:ital@1&family=Alegreya+Sans+SC:wght@800&family=Cabin:wght@500&display=swap" rel="stylesheet">
<style>
  :root{
    --page:#eeeeec;
    --panel:#f4f2ef;
    --orange:#e8731c;
    --orange-deep:#c8631f;
    --band-top:#d47b38;
    --band-bottom:#e09a58;
    --tab:#e2b48b;
    --ink:#1d1d1d;
    --body:#333;
    --rule:#dcdad6;
    --footer-top:#c66a25;
    --footer-bottom:#dd9048;
    --footer-text:#f5e3cf;
  }
  *{box-sizing:border-box;margin:0;padding:0}
  html,body{width:1200px;height:988px;overflow:hidden}
  body{background:var(--page);position:relative;font-family:"Gelasio",Georgia,serif}

  .brand{position:absolute;left:434px;top:24px;height:98px;display:flex;align-items:center;gap:14px}
  .brand-dot{width:96px;height:96px;border-radius:50%;background:var(--orange)}
  .brand-name{font-family:"Squada One",sans-serif;font-size:64px;color:var(--ink);line-height:1}

  .nav-tab{position:absolute;left:349px;top:134px;width:477px;height:14px}
  .nav-band{position:absolute;left:0;top:147px;width:1200px;height:33px;
    background:linear-gradient(var(--band-top),var(--band-bottom))}
  .nav{position:absolute;top:0;left:0;width:100%;height:33px;display:flex;justify-content:center;align-items:center;list-style:none;
    font-family:"Alegreya Sans SC",sans-serif;font-weight:800;font-size:13px;padding-left:14px}
  .nav li{color:var(--ink);padding:0 18px;position:relative}
  .nav li+li::before{content:"";position:absolute;left:0;top:3px;width:2px;height:9px;background:#b5261b}
  .nav li.is-current{color:#fff}

  .panel{position:absolute;background:var(--panel)}
  .intro{left:180px;top:212px;width:556px;height:179px;padding:0 8px}
  .section-title{font-family:"Squada One",sans-serif;color:var(--orange);font-size:22px;font-weight:400;line-height:1}
  .intro .section-title{margin-top:14px;margin-bottom:9px}
  .copy{font-style:italic;font-size:10.6px;line-height:21px;color:var(--body);text-align:justify}
  .intro .copy{height:126px;overflow:hidden}

  .photo{position:absolute;left:747px;top:212px;width:272px;height:182px;
    background:linear-gradient(135deg,#d9d4cc 0%,#eef0f0 40%,#c9ccce 70%,#9aa0a5 100%);
    box-shadow:0 4px 4px -2px rgba(190,120,60,.6)}
  .slider-arrows{position:absolute;left:858px;top:400px;width:48px;height:14px}

  .feature-title{position:absolute;left:188px;top:411px}
  .feature{left:180px;top:436px;width:839px;height:236px;padding:6px 7px 0 8px}
  .feature .copy+.copy{margin-top:8px}

  .questions{position:absolute;left:537px;top:748px;width:127px;height:84px}
  .divider{position:absolute;left:180px;top:836px;width:839px;height:1px;background:var(--rule)}

  .footer{position:absolute;left:0;top:878px;width:1200px;height:110px;
    background:linear-gradient(var(--footer-top),var(--footer-bottom))}
  .footer-links{display:flex;justify-content:center;list-style:none;margin-top:11px;
    font-family:"Gelasio",Georgia,serif;font-style:normal;font-size:9px;color:var(--footer-text);letter-spacing:.2px}
  .footer-links li{padding:0 8px;position:relative}
  .footer-links li+li::before{content:"|";position:absolute;left:-2px}
  .social{display:flex;justify-content:center;gap:36px;list-style:none;margin-top:24px}
  .social li{width:24px;height:24px;border-radius:50%;background:#f6e6d6}
</style>
</head>
<body>
  <header>
    <div class="brand">
      <span class="brand-dot"></span>
      <span class="brand-name">ZipRoam</span>
    </div>
    <svg class="nav-tab" viewBox="0 0 477 14" aria-hidden="true">
      <path d="M0 14 L70 0 H407 L477 14 Z" fill="var(--tab)"/>
    </svg>
    <nav class="nav-band">
      <ul class="nav">
        <li class="is-current">Home</li>
        <li>About Us</li>
        <li>Our Solutions</li>
        <li>Contact Us</li>
      </ul>
    </nav>
  </header>

  <main>
    <section class="panel intro">
      <h2 class="section-title">ZipRoam for Hotels</h2>
      <p class="copy">Lorem ipsum dolor sit amet, consectetur adipiscing elit. Proin tempus dolor vitae purus tincidunt nec iaculis ipsum mollis. Cras at nulla a arcu placerat cursus bibendum sit amet massa. Phasellus fermentum, nibh eu ullamcorper viverra, risus mi tempor est, sed sodales ante orci ac turpis. Etiam mattis nulla non leo rutrum blandit. Donec sit amet gravida est. Vivamus in magna eget erat iaculis iaculis. Cras lacinia, justo ac pellentesque placerat, nunc tortor commodo justo, non cursus leo sem nec metus. Quisque eget ultrices arcu. Aliquam porta elementum metus ut mattis. Nulla a risus ac turpis luctus facilisis sed id purus. Phasellus suscipit, mauris id suscipit sodales, mi ipsum tristique ante.</p>
    </section>

    <div class="photo" role="img" aria-label="Photo of a woman on a mobile phone working at a desk with a computer"></div>
    <svg class="slider-arrows" viewBox="0 0 48 14" aria-label="Slider controls">
      <path d="M10 2 L4 7 L10 12" fill="none" stroke="var(--orange)" stroke-width="2.5"/>
      <path d="M38 2 L44 7 L38 12" fill="none" stroke="var(--orange)" stroke-width="2.5"/>
    </svg>

    <h2 class="section-title feature-title">Lorem ipsum dolor sit amet</h2>
    <section class="panel feature">
      <p class="copy">Lorem ipsum dolor sit amet, consectetur adipiscing elit. Proin tempus dolor vitae purus tincidunt nec iaculis ipsum mollis. Cras at nulla a arcu placerat cursus bibendum sit amet massa. Phasellus fermentum, nibh eu ullamcorper viverra, risus mi tempor est, sed sodales ante orci ac turpis. Etiam mattis nulla non leo rutrum blandit. Donec sit amet gravida est. Vivamus in magna eget erat iaculis iaculis. Cras lacinia, justo ac pellentesque placerat, nunc tortor commodo justo, non cursus leo sem nec metus. Quisque eget ultrices arcu. Aliquam porta elementum metus ut mattis. Nulla a risus ac turpis luctus facilisis sed id purus. Phasellus suscipit, mauris id suscipit sodales, mi ipsum tristique ante, quis lacinia dui dolor eget mauris. Praesent imperdiet leo eu metus interdum porta. Donec porta hendrerit elit, nec semper magna elementum id.</p>
      <p class="copy">Lorem ipsum dolor sit amet, consectetur adipiscing elit. Proin tempus dolor vitae purus tincidunt nec iaculis ipsum mollis. Cras at nulla a arcu placerat cursus bibendum sit amet massa. Phasellus fermentum, nibh eu ullamcorper viverra, risus mi tempor est, sed sodales ante orci ac turpis. Etiam mattis nulla non leo rutrum blandit. Donec sit amet gravida est. Vivamus in magna eget erat iaculis iaculis. Cras lacinia, justo ac pellentesque placerat, nunc tortor commodo justo, non cursus leo sem nec metus. Quisque eget ultrices arcu. Aliquam porta elementum metus ut mattis. Nulla a risus ac turpis luctus facilisis sed id purus. Phasellus suscipit, mauris id suscipit sodales, mi ipsum tristique ante, quis lacinia dui dolor eget mauris. Praesent imperdiet leo eu metus interdum porta. Donec porta hendrerit elit, nec semper magna elementum id.</p>
    </section>

    <svg class="questions" viewBox="0 0 127 84" aria-label="Questions?">
      <defs>
        <linearGradient id="cloudFill" x1="0" y1="0" x2="0" y2="1">
          <stop offset="0" stop-color="#f6b877"/>
          <stop offset="0.55" stop-color="#e27a2c"/>
          <stop offset="1" stop-color="#c85a16"/>
        </linearGradient>
      </defs>
      <path d="M18 83 C6 83 1 74 2 64 C3 52 12 46 22 47 C22 30 32 22 44 24 C50 8 62 1 72 1 C88 1 98 12 100 28 C112 28 120 36 118 48 C126 52 127 62 125 70 C122 79 115 83 106 83 Z" fill="url(#cloudFill)" stroke="#c8631f" stroke-width="1"/>
      <text x="63.5" y="63" text-anchor="middle" font-family="Cabin, sans-serif" font-weight="500" font-size="17" fill="#9a4a14">Questions?</text>
    </svg>

    <div class="divider"></div>
  </main>

  <footer class="footer">
    <ul class="footer-links">
      <li>PRIVACY POLICY</li>
      <li>TERMS OF SERVICES</li>
      <li>SUPPORT</li>
    </ul>
    <ul class="social">
      <li role="img" aria-label="Social network link"></li>
      <li role="img" aria-label="Social network link"></li>
      <li role="img" aria-label="Social network link"></li>
      <li role="img" aria-label="News feed link"></li>
      <li role="img" aria-label="Video channel link"></li>
    </ul>
  </footer>
</body>
</html>
```